Web site for cutting edge executive coaching and consulting firm | ||
Bravonte | ||
Consulting | ||
Services that increase Performance: - Coaching: Executives, Groups / Teams - Problem Solving - Organizational Change. Focus on: - Holistic approach - Verdessan spirit (colors) - Psychological driven models - Relationship building - sustained outcomes |
I like colors, yet, colors shall not hinder clear reading of text. I like a clear & simple structure of Website. I like to use symbols and/or forms. |
Cutting-Edge Unique/Creative Clean/Simple Professional Exciting Industrial Colorful Elegant Progressive Service Oriented Traditional |
blue | ||
Arial Verdana |

```html
<!DOCTYPE html>
<html lang="en">
<head>
<meta charset="utf-8">
<title>Bravonte Consulting</title>
<link href="https://fonts.googleapis.com/css2?family=Arimo:wght@400;700&display=swap" rel="stylesheet">
<style>
  :root {
    --brand-blue: #1f5fb0;
    --deep-blue: #0d3f8a;
    --sky-blue: #2aa2e6;
    --nav-top: #2f7fd6;
    --nav-bottom: #0f4fa8;
    --accent-red: #d4262c;
    --text-grey: #555a60;
    --rule-grey: #cfd4da;
    --footer-grey: #8e9195;
    --white: #ffffff;
  }
  * { box-sizing: border-box; margin: 0; padding: 0; }
  html, body { width: 1200px; height: 790px; overflow: hidden; background: var(--white); }
  body { font-family: "Arimo", Arial, sans-serif; color: var(--text-grey); position: relative; }

  .site-header { position: absolute; left: 0; top: 0; width: 1200px; height: 103px; background: var(--white); }
  .brand-name { position: absolute; left: 216px; top: 28px; font-size: 56px; font-weight: 700; color: var(--brand-blue); letter-spacing: -1px; line-height: 1; }
  .header-contact { position: absolute; left: 826px; top: 52px; display: flex; align-items: center; gap: 14px; }
  .header-contact svg { width: 40px; height: 40px; }
  .header-contact .label { font-size: 17px; color: var(--deep-blue); line-height: 1.2; }
  .header-contact .phone { font-size: 20px; font-weight: 700; color: var(--deep-blue); }

  .main-nav { position: absolute; left: 0; top: 103px; width: 1200px; height: 34px; background: linear-gradient(var(--nav-top), var(--nav-bottom)); }
  .main-nav ul { list-style: none; position: absolute; left: 211px; top: 0; display: flex; height: 34px; }
  .main-nav li { font-size: 14px; color: var(--white); line-height: 34px; padding: 0 28px; border-right: 1px solid rgba(255,255,255,0.25); }
  .main-nav li.active { background: linear-gradient(#5aa8f0, #2a78d0); }

  .hero-band { position: absolute; left: 0; top: 137px; width: 1200px; height: 319px;
    background: radial-gradient(ellipse at 50% 40%, #6fd0ff 0%, var(--sky-blue) 35%, #1570c8 75%, #0c4f9e 100%); }
  .hero-panel { position: absolute; left: 209px; top: 144px; width: 782px; height: 283px; background: linear-gradient(#ffffff, #eef3f8); border: 2px solid #d9e6f2; }
  .hero-photo { position: absolute; left: 290px; top: 0; width: 488px; height: 279px; background: linear-gradient(90deg, rgba(238,243,248,0), #c9d3dd 30%, #b6c2cd 70%, #e3e9ef); }
  .hero-title { position: absolute; left: 22px; top: 82px; font-size: 20px; font-weight: 700; color: var(--deep-blue); line-height: 1.25; }
  .hero-title em { font-style: normal; color: var(--accent-red); }
  .hero-text { position: absolute; left: 22px; top: 136px; width: 270px; font-size: 10.5px; line-height: 1.3; color: #333; }
  .learn-more { position: absolute; left: 22px; top: 202px; width: 145px; height: 38px; border-radius: 6px; background: linear-gradient(#6b7075, #3c4044); color: var(--white); font-size: 15px; font-weight: 700; text-align: center; line-height: 34px; border: 2px solid #c3c8cc; }
  .slider-dots { position: absolute; left: 28px; top: 264px; display: flex; gap: 6px; }
  .slider-dots span { width: 12px; height: 12px; border-radius: 50%; background: var(--brand-blue); }
  .slider-dots span.off { background: #dfe6ee; border: 1px solid #b8c4d0; }

  .content h2 { position: absolute; font-size: 18px; font-weight: 700; color: var(--brand-blue); }
  .content h3 { position: absolute; font-size: 12px; font-weight: 700; color: var(--deep-blue); letter-spacing: 0.5px; }
  .divider { position: absolute; top: 468px; width: 1px; height: 200px; background: var(--rule-grey); }
  .small-text { position: absolute; font-size: 10.5px; line-height: 1.35; color: var(--text-grey); }
  .read-more { position: absolute; font-size: 10.5px; color: var(--brand-blue); text-decoration: underline; }
  .welcome-photo { position: absolute; left: 221px; top: 497px; width: 96px; height: 72px; background: linear-gradient(#e4e9ee, #b9c4cf); border: 1px solid var(--rule-grey); }
  .service-list { position: absolute; left: 617px; top: 538px; list-style: none; }
  .service-list li { font-size: 10.5px; line-height: 17px; color: var(--text-grey); padding-left: 14px; position: relative; }
  .service-list li::before { content: ""; position: absolute; left: 0; top: 6px; width: 6px; height: 6px; background: var(--accent-red); }
  .contact-form .field { position: absolute; left: 810px; width: 180px; height: 20px; border: 1px solid #a9b0b8; background: var(--white); font-size: 10.5px; padding: 3px 5px; color: #333; }
  .contact-form .field.comment { height: 48px; }
  .send-button { position: absolute; left: 810px; top: 638px; width: 138px; height: 24px; border-radius: 5px; background: linear-gradient(#6b7075, #3c4044); color: var(--white); font-size: 10.5px; font-weight: 700; text-align: center; line-height: 24px; }

  .site-footer { position: absolute; left: 0; top: 708px; width: 1200px; height: 82px; background: var(--footer-grey); text-align: center; color: var(--white); }
  .footer-links { margin-top: 12px; font-size: 11.5px; }
  .copyright { margin-top: 10px; font-size: 10.5px; }
</style>
</head>
<body>
  <header class="site-header">
    <div class="brand-name">Bravonte</div>
    <div class="header-contact">
      <svg viewBox="0 0 40 40" aria-hidden="true">
        <circle cx="20" cy="20" r="19" fill="#0d3f8a"/>
        <path d="M14 10c1.5-1 3 0 3.6 1.6l1 3c.4 1-.2 2-1 2.6l-1 .8c.8 2.6 2.8 4.6 5.4 5.4l.8-1c.6-.8 1.6-1.4 2.6-1l3 1c1.6.6 2.6 2.1 1.6 3.6-1.6 2.4-4 3-6.4 2-5.4-2.2-9.6-6.4-11.8-11.8-1-2.4-.4-4.8 2.2-6.2z" fill="#fff"/>
      </svg>
      <div>
        <div class="label">Contact us</div>
        <div class="phone">1800-555-0142</div>
      </div>
    </div>
  </header>

  <nav class="main-nav">
    <ul>
      <li class="active">Home</li>
      <li>About Us</li>
      <li>Our Services</li>
      <li>Testimonials</li>
      <li>Contact Us</li>
    </ul>
  </nav>

  <section class="hero-band"></section>
  <section class="hero-panel">
    <div class="hero-photo" role="img" aria-label="Photo of a smiling team of five business professionals standing with arms crossed"></div>
    <h1 class="hero-title">Lorem ipsum dolor <em>sit amet,</em><br><em>consectetuer adipiscing elit</em></h1>
    <p class="hero-text">Lorem ipsum dolor sit amet, consectetuer adipiscing elit, sed diam nonummy nibh euismod tincidunt ut laoreet dolore magna aliquam erat volutpat.</p>
    <div class="learn-more">LEARN MORE</div>
    <div class="slider-dots"><span></span><span></span><span></span><span></span><span class="off"></span></div>
  </section>

  <main class="content">
    <h2 style="left:216px; top:466px;">Welcome to Bravonte Consulting</h2>
    <div class="welcome-photo" role="img" aria-label="Photo of colleagues meeting around a laptop"></div>
    <p class="small-text" style="left:330px; top:497px; width:250px;">Lorem ipsum dolor sit amet, consectetuer adipiscing elit, sed diam nonummy nibh euismod tincidunt ut laoreet dolore magna aliquam erat volutpat. Ut wisi enim ad minim veniam.</p>
    <p class="small-text" style="left:216px; top:586px; width:370px;">Duis autem vel eum iriure dolor in hendrerit in vulputate velit esse molestie consequat, vel illum dolore eu feugiat nulla facilisis at vero eros et accumsan et iusto odio dignissim qui blandit praesent luptatum zzril delenit augue duis dolore te feugait nulla facilisi.</p>
    <span class="read-more" style="left:216px; top:646px;">read more</span>

    <div class="divider" style="left:600px;"></div>

    <h3 style="left:617px; top:470px;">OUR SERVICES</h3>
    <p class="small-text" style="left:617px; top:497px; width:165px;">Lorem ipsum dolor sit amet, consectetuer adipiscing elit</p>
    <ul class="service-list">
      <li>Lorem ipsum dolor sit amet</li>
      <li>Lorem ipsum dolor sit amet</li>
      <li>Lorem ipsum dolor sit amet</li>
      <li>Lorem ipsum dolor sit amet</li>
    </ul>
    <span class="read-more" style="left:617px; top:630px;">read more</span>

    <div class="divider" style="left:799px;"></div>

    <h3 style="left:816px; top:470px;">CONTACT US</h3>
    <form class="contact-form">
      <div class="field" style="top:500px;">Name</div>
      <div class="field" style="top:527px;">Email</div>
      <div class="field" style="top:554px;">Phone</div>
      <div class="field comment" style="top:581px;">Comment</div>
      <div class="send-button">SEND YOUR REQUEST</div>
    </form>
  </main>

  <footer class="site-footer">
    <div class="footer-links">Home &nbsp;|&nbsp; About Us &nbsp;|&nbsp; Our Services &nbsp;|&nbsp; Testimonials &nbsp;|&nbsp; Contact Us</div>
    <div class="copyright">copyright Bravonte Consulting. All rights reserved.</div>
  </footer>
</body>
</html>
```